Make a website for Velmora, a Luxury and Modern Concierge Platform based in the UAE

Concierge Platform that has various luxury and exotic actives available to clients, itinerary planning for a dubai / uae based holiday.
Want the website to appear luxury, modern and easy to understand, with a landing page that can captivate customers, majority will use Mobile but Desktop should look good too. Whatsapp Contact pop-out, and email sign up list. Social Link (Facebook, Instagram, Whatsapp, Whatsapp Broadcast, Twitter/X, etc).
Ability to make it Dark and Light themed.
Second page Page that has a list of activities on a drop down/ list, as follows:
Flights
Car Rental
Luxury Car Rental
Chauffer
Yachts/ Boats
Jet Ski / Watersports
Buggies/ ATV
Dining
Tickets/Events
Apartments/ Hotels
Personal Shopping.
Link to competitors, who's websites appear basic and could be 100% improved, for examples:
- https://www.quietharbourstays.example/
- https://www.tivra.example/
- https://www.gulf-latch.example/
- https://thelomarenhouse.example/dubai.html
- https://www.theplatinumhostdesk.example/concierge-service-dubai/
Open to logo designs, we own Velmora.com.
Colours:
Luxury Style, Black and Gold is often used, but maybe over-used?
A modern colour palette White, Light Blue, Light Grey, but we aren't experts at this, so this isn't by any means strict criteria, let the creative mind run free.
Thank you

```html
<!DOCTYPE html>
<html lang="en">
<head>
<meta charset="utf-8">
<title>Velmora — Luxury Concierge</title>
<link href="https://fonts.googleapis.com/css2?family=Antonio:wght@400;600;700&family=Pathway+Gothic+One&display=swap" rel="stylesheet">
<style>
  :root {
    --ink: #050403;
    --cream: #fbf0dc;
    --paper: #fff7ea;
    --gold-deep: #3a2a08;
    --gold-mid: #6b4c10;
    --rule: rgba(235, 225, 210, 0.75);
  }
  * { margin: 0; padding: 0; box-sizing: border-box; }
  html, body {
    width: 702px;
    height: 1200px;
    overflow: hidden;
    background: var(--ink);
  }
  .hero {
    position: relative;
    width: 702px;
    height: 1200px;
    overflow: hidden;
    color: var(--cream);
  }
  .hero-backdrop {
    position: absolute;
    inset: 0;
    background:
      radial-gradient(ellipse 60% 30% at 60% 32%, rgba(140, 100, 25, 0.55), transparent 70%),
      radial-gradient(ellipse 50% 20% at 35% 75%, rgba(120, 80, 20, 0.35), transparent 70%),
      linear-gradient(180deg, #1a1408 0%, #2c2009 25%, #1f1706 50%, #120d05 75%, #050403 100%);
  }
  .site-header {
    position: absolute;
    top: 0; left: 0; right: 0;
    height: 145px;
    border-bottom: 2px solid var(--rule);
  }
  .brand {
    position: absolute;
    left: 36px;
    top: 70px;
    display: flex;
    align-items: center;
    gap: 12px;
  }
  .brand-mark {
    width: 32px; height: 32px;
    border-radius: 50%;
    background: var(--gold-mid);
  }
  .brand-name {
    font-family: "Antonio", sans-serif;
    font-weight: 700;
    font-size: 24px;
    letter-spacing: 0.5px;
    color: var(--paper);
  }
  .menu-toggle {
    position: absolute;
    right: 42px;
    top: 72px;
    width: 60px;
    height: 34px;
  }
  .hero-title {
    position: absolute;
    left: 62px;
    top: 572px;
    font-family: "Antonio", sans-serif;
    font-weight: 600;
    font-size: 178px;
    line-height: 1;
    letter-spacing: -1px;
    color: var(--cream);
  }
  .hero-intro {
    position: absolute;
    left: 70px;
    top: 834px;
    width: 530px;
    font-family: "Pathway Gothic One", sans-serif;
    font-size: 21px;
    line-height: 33px;
    color: #fbe6b4;
  }
  .cta-link {
    position: absolute;
    left: 70px;
    top: 1046px;
    display: flex;
    align-items: center;
    gap: 14px;
    font-family: "Pathway Gothic One", sans-serif;
    font-size: 25px;
    color: var(--paper);
    text-decoration: none;
  }
</style>
</head>
<body>
  <main class="hero">
    <div class="hero-backdrop" role="img" aria-label="Dimly lit luxury lounge bar with warm golden ceiling lights and bottle shelves"></div>

    <header class="site-header">
      <div class="brand">
        <span class="brand-mark"></span>
        <span class="brand-name">VELMORA</span>
      </div>
      <svg class="menu-toggle" viewBox="0 0 60 34" aria-label="Menu">
        <rect x="0" y="0" width="60" height="5" fill="#f6ecdc"/>
        <rect x="0" y="14.5" width="60" height="5" fill="#f6ecdc"/>
        <rect x="0" y="29" width="60" height="5" fill="#f6ecdc"/>
      </svg>
    </header>

    <h1 class="hero-title">VELMORA</h1>

    <p class="hero-intro">Lorem ipsum dolor, sit amet consectetur adipisicing elit. Laudantium autem hic dignissimos amet distinctio culpa repellendus consequatur blanditiis sint quas, saepe consequuntur quidem accusantium debitis et nesciunt deleniti eos molestiae!</p>

    <a class="cta-link" href="#contact">
      Get in touch
      <svg width="18" height="18" viewBox="0 0 18 18" fill="none" stroke="#f6ecdc" stroke-width="2">
        <path d="M8 2H2v14h14v-6"/>
        <path d="M11 1h6v6"/>
        <path d="M17 1L8 10"/>
      </svg>
    </a>
  </main>
</body>
</html>
```